Ground breaking athletic gear company needs a kick ass business card

We are an American start up athletic gear company that uses a medically proven biohack to boost athletic performance. Heat kills strength and endurance. Our gear helps athletes manage heat better and ultimatley can improve them by up to 10% instantly. Nothing like it out there! Launching this summer.
We are looking for a modern, minimalist design that captures a sporty edge. Check out www.vanteluxgear.com, @vanteluxgear on pictorama for more ideas.

Target Market(s)

25-35 year olds, male and female athletes, vortexlift athletes, competitive runners

Industry/Entity Type

Business

Contact Information for Business Card

Derek Hollins
Founder
derekh@vanteluxgear.com
www.VanteluxGear.com
+1 (555) 014-2286

Font styles to use
Sans Serif

Requirements
Must have
• Logo and icon
• All contact information
• derekh@vanteluxgear.com
• +1 (555) 019-4431 M
• +1 (555) 014-2286
Nice to have
• Tag line : "Chill & Charge"

```html
<!DOCTYPE html>
<html lang="en">
<head>
<meta charset="utf-8">
<title>Vantelux Gear — Business Card</title>
<link rel="stylesheet" href="https://fonts.googleapis.com/css2?family=Montserrat:wght@400;500;700&display=swap">
<style>
  :root {
    --page: #ebe8e4;
    --card: #030405;
    --yellow: #fad907;
    --white: #ffffff;
    --blue: #3d84c6;
    --ink: #0a0a0a;
  }
  * { margin: 0; padding: 0; box-sizing: border-box; }
  html, body { width: 1200px; height: 1000px; overflow: hidden; }
  body {
    background: var(--page);
    font-family: "Montserrat", Arial, sans-serif;
    position: relative;
  }
  .card {
    position: absolute;
    width: 516px;
    height: 292px;
    background: var(--card);
    overflow: hidden;
  }
  .card--front { left: 350px; top: 217px; }
  .card--back { left: 351px; top: 536px; height: 294px; }

  .accent-area {
    position: absolute;
    left: 28px; top: 26px;
    width: 212px; height: 244px;
  }
  .tagline {
    position: absolute;
    left: 28px; top: 26px;
    width: 212px; height: 244px;
    display: flex; flex-direction: column; justify-content: center; align-items: center;
    color: var(--ink);
    font-weight: 700;
    line-height: 1.15;
    text-align: center;
  }
  .tagline__first { font-size: 26px; }
  .tagline__amp { font-size: 20px; }
  .tagline__second { font-size: 18px; letter-spacing: 1px; }

  .identity { position: absolute; left: 294px; top: 25px; color: var(--white); }
  .identity__name { font-size: 19px; font-weight: 700; letter-spacing: 0.3px; }
  .identity__role { font-size: 15px; font-weight: 500; margin-top: 1px; }

  .contact {
    position: absolute; left: 294px; top: 218px;
    list-style: none;
    color: var(--yellow);
    font-size: 13.5px; font-weight: 500;
    line-height: 19px;
    white-space: nowrap;
  }

  .wordmark {
    position: absolute; left: 0; right: 0; top: 92px;
    text-align: center;
    color: var(--blue);
    font-weight: 500;
  }
  .wordmark__main { font-size: 48px; letter-spacing: 6px; line-height: 1; }
  .wordmark__sub { font-size: 28px; letter-spacing: 5px; margin-top: 10px; line-height: 1; }
</style>
</head>
<body>
  <section class="card card--front">
    <svg class="accent-area" viewBox="0 0 212 244" role="img" aria-label="Yellow and white angular accent area behind the tagline">
      <rect width="212" height="244" fill="#fad907"/>
    </svg>
    <div class="tagline">
      <span class="tagline__first">CHILL</span>
      <span class="tagline__amp">&amp;</span>
      <span class="tagline__second">CHARGE</span>
    </div>

    <div class="identity">
      <p class="identity__name">DEREK HOLLINS</p>
      <p class="identity__role">Founder</p>
    </div>

    <ul class="contact">
      <li>+1 (555) 014-2286</li>
      <li>derekh@vanteluxgear.com</li>
      <li>www.VanteluxGear.com</li>
    </ul>
  </section>

  <section class="card card--back">
    <div class="wordmark">
      <p class="wordmark__main">VANTELUX</p>
      <p class="wordmark__sub">GEAR</p>
    </div>
  </section>
</body>
</html>
```